Upscale Children's Boutique Needs a PSD Web Design

We need a PSD web design for an online children's boutique called 'Mavoret'. We specialize in special occasion wear for infants. Our apparel products are typically selected for christening & baptisms, birthdays, holidays and weddings. We would like to see designs that compliment our existing logo and business card. The final design should communicate a sense of luxury, but also be fun and oriented towards children.
Our current website is www.mavoret.com. Note: Not all products are loaded.
Changes to the color scheme, fonts, background and graphics are welcome. And while we like the layout of my current TrellaCart theme (Seashore), we do expect that SMALL modifications will be needed to make it ours. For example, we would like the cart to be placed more visibly. I have a designer that can code the changes you come up with so feel free to suggest what you feel is best.
We look forward to your designs. Good luck!
Websites we like:
https://www.shopwrenfig.com/ (The layout of this site is nice to me)
http://www.elsiesattic.com/
http://www.quietmeadowherbals.com/
Updates
This contest is for PSD design only. No Trellacart development or coding is required.
Target Market(s)
Our typical customer is female age 20-45 shopping for her own child or for a gift.
Industry/Entity Type
Boutique
Requirements
Must have
- PSD Design
- These 5 items listed below are things we’d like:
- (1) General styling (color scheme, fonts, background, graphics, etc.) & layout
- • ONLY the logo colors are set … feel free to add colors that compliment it
- • Prefer narrow (or single line) footer
- • We think the main banner/image is too large
- (2) Create main banner/image (current template uses 970px wide)
- (3) AT LEAST Three (3) Marketing banners (current template uses 433 x 225):
- • Our Hottest Products
- • Our Newest Arrivals
- • Newsletter sign-up
- (4) Border to enclose admin links (My account, Gift Certificates, Create an Account)
- (5) New badges / icon / images
- • Shopping Cart --> Bag or cart image should stand out; try to place above search bar (you’ll have to lower the search bar to do this)
- • Sale Badge --> anything goes. Could be a badge or a sash. Might also be nice to have these for the bestsellers as well.
- • Star Icons for product reviews (optional) --> Keep the stars just have them be more stylized
Nice to have
- We like pages that have a background and think one might look good on our site if not too busy.
Should not have
- We do not like extremely dark backgrounds for web pages.

```html
<!DOCTYPE html>
<html lang="en">
<head>
<meta charset="utf-8">
<title>Mavoret – Special Occasion Wear for Infants</title>
<link rel="stylesheet" href="https://fonts.googleapis.com/css2?family=Open+Sans:wght@400;600;700&family=Great+Vibes&display=swap">
<style>
:root{
  --teal:#5fc3be;
  --teal-dark:#3fa9a4;
  --teal-soft:#8fd6d2;
  --coral:#f3907f;
  --coral-soft:#f7b8ab;
  --ink:#555a5c;
  --muted:#9a9fa1;
  --line:#e3e6e6;
  --paper:#ffffff;
  --page:#f5f5f3;
}
*{box-sizing:border-box;margin:0;padding:0}
html,body{width:769px;height:1200px;overflow:hidden}
body{background:var(--page);font-family:"Open Sans",Arial,sans-serif;color:var(--ink);font-size:9px;position:relative}
a{color:inherit;text-decoration:none}

.topbar{height:20px;background:var(--teal);display:flex;align-items:center;justify-content:space-between;padding:0 44px}
.topbar .social{display:flex;gap:6px}
.topbar .social span{width:9px;height:9px;border-radius:50%;background:#fff;opacity:.85}
.topbar .account{display:flex;font-size:6.5px;color:#fff;letter-spacing:.4px;text-transform:uppercase}
.topbar .account a{padding:0 7px;border-left:1px solid rgba(255,255,255,.5)}
.topbar .account a:first-child{border-left:0}

.header{height:92px;position:relative;background:var(--paper)}
.header .phone{position:absolute;left:66px;top:40px;font-size:8px;color:var(--coral);line-height:1.5}
.header .phone b{font-weight:600}
.header .phone small{display:block;color:var(--muted);font-size:6.5px}
.brand{position:absolute;left:50%;top:24px;transform:translateX(-50%);display:flex;align-items:center;gap:8px}
.brand .dot{width:26px;height:26px;border-radius:50%;background:var(--teal)}
.brand .name{font-size:25px;font-weight:600;color:var(--teal-dark);letter-spacing:1px}
.basket{position:absolute;right:60px;top:40px;width:108px;height:28px;background:var(--teal);border-radius:3px;display:flex;align-items:center;gap:7px;padding-left:10px;color:#fff;font-size:8.5px;font-weight:600}

.nav{height:28px;background:var(--paper);border-top:1px solid var(--line);border-bottom:1px solid var(--line);display:flex;align-items:center;justify-content:space-between;padding:0 70px}
.nav ul{list-style:none;display:flex;gap:22px;font-size:8.5px;color:var(--ink)}
.search{width:112px;height:15px;border:1px solid var(--line);display:flex;align-items:center;justify-content:space-between;padding:0 5px;font-size:6.5px;color:var(--muted)}

.perks{display:flex;justify-content:center;gap:48px;padding:14px 0 8px}
.perk{display:flex;align-items:center;gap:9px}
.perk .icon{width:34px;height:34px;border-radius:50%;background:var(--teal-soft);display:flex;align-items:center;justify-content:center}
.perk h3{font-size:13px;font-weight:700;color:var(--ink);line-height:1.1}
.perk p{font-size:7.5px;color:var(--muted)}

.hero{position:relative;margin:8px 44px 0;height:280px;display:flex}
.hero .photo{width:300px;height:100%;background:linear-gradient(160deg,#f6f6f4,#e9e7e2)}
.hero .panel{flex:1;position:relative;background:linear-gradient(180deg,#8cd3cf,#6cc6c1);border-radius:0 6px 6px 0}
.hero .copy{position:absolute;left:70px;top:58px;color:#fff}
.hero .title{display:inline-block;font-family:"Great Vibes",cursive;font-size:44px;color:var(--coral);line-height:1.2;background:#fff;padding:0 16px;border-radius:3px}
.hero .deal{font-size:15px;margin-top:10px}
.hero .deal b{font-size:22px}
.hero .blurb{font-size:7.5px;line-height:1.5;margin-top:6px;max-width:210px}
.btn{display:inline-block;background:var(--coral);color:#fff;font-weight:600;border-radius:2px}
.hero .btn{margin-top:14px;font-size:12px;padding:6px 18px}
.hero .sprig{position:absolute;right:20px;bottom:16px;width:60px;height:60px;border-radius:50%;background:rgba(255,255,255,.25)}
.dots{display:flex;justify-content:center;gap:5px;margin-top:8px}
.dots span{width:7px;height:7px;border-radius:50%;background:#c9cccc}
.dots span:first-child{background:var(--ink)}

.promos{display:flex;gap:12px;margin:26px 44px 0}
.promo{flex:1;height:86px;display:flex;background:var(--paper);box-shadow:0 1px 2px rgba(0,0,0,.08)}
.promo .pic{width:92px;background:linear-gradient(150deg,#f3e2d6,#e6cfc0)}
.promo .txt{flex:1;display:flex;flex-direction:column;justify-content:center;align-items:center;text-align:center;padding:0 6px}
.promo h4{font-size:15px;font-weight:700;color:var(--ink);line-height:1.05;text-transform:uppercase}
.promo h4 em{font-style:normal;color:var(--coral)}
.promo p{font-size:8px;color:var(--teal-dark)}
.promo .btn{font-size:6.5px;padding:3px 8px;margin-top:4px}

.featured{margin:24px 44px 0}
.featured h2{text-align:center;font-size:19px;font-weight:600;color:var(--teal-dark);letter-spacing:1px;position:relative}
.featured h2::before,.featured h2::after{content:"";position:absolute;top:50%;width:180px;height:1px;background:var(--line)}
.featured h2::before{left:0}.featured h2::after{right:0}
.grid{display:flex;gap:18px;margin-top:30px;padding:0 20px}
.card{flex:1;background:var(--paper);border:1px solid var(--line);padding:10px 10px 12px;text-align:center}
.card .pic{height:108px;background:linear-gradient(180deg,#fbfbfb,#eef0f0)}
.card h5{font-size:7.5px;font-weight:600;margin-top:10px}
.card .price{font-size:15px;color:var(--coral);margin-top:6px}
.card p{font-size:6.5px;color:var(--muted);line-height:1.4;margin-top:2px}
.card .btn{display:block;font-size:6.5px;padding:5px 0;margin-top:10px;letter-spacing:.4px;text-transform:uppercase}

.footer{position:absolute;left:0;right:0;bottom:0;height:236px;background:var(--teal);color:#fff;border-top:4px solid var(--teal-soft)}
.footer .cols{display:flex;padding:34px 70px 0;gap:46px}
.footer h6{font-size:10px;font-weight:600;margin-bottom:6px}
.footer ul{list-style:none;font-size:7px;line-height:1.65;opacity:.95}
.footer .social{display:flex;gap:6px;margin-bottom:14px}
.footer .social span{width:10px;height:10px;border-radius:50%;background:#fff}
.footer input{display:block;width:108px;height:15px;border:0;margin-bottom:5px;font:6.5px "Open Sans",sans-serif;padding:0 5px;color:var(--muted)}
.footer .btn{font-size:6.5px;padding:3px 12px}
.footer .legal{position:absolute;bottom:0;left:0;right:0;height:22px;background:var(--teal-dark);text-align:center;font-size:6.5px;line-height:22px}
</style>
</head>
<body>

<div class="topbar">
  <div class="social"><span></span><span></span><span></span></div>
  <nav class="account"><a href="#">My Account</a><a href="#">Gift Certificates</a><a href="#">Create an Account</a></nav>
</div>

<header class="header">
  <div class="phone"><b>Phone orders:</b> (555) 014-2386<small>Mon to Fri 9am – 5pm EST</small></div>
  <a class="brand" href="#"><span class="dot"></span><span class="name">Mavoret</span></a>
  <a class="basket" href="#">
    <svg width="12" height="12" viewBox="0 0 12 12"><path d="M2 4h8l-1 7H3z" fill="none" stroke="#fff" stroke-width="1.2"/><path d="M4 4V3a2 2 0 0 1 4 0v1" fill="none" stroke="#fff" stroke-width="1.2"/></svg>
    Your Basket (0)
  </a>
</header>

<nav class="nav">
  <ul><li>New Baby</li><li>Christening &amp; Baptism</li><li>Birthday</li><li>Holiday</li><li>Wedding</li></ul>
  <div class="search"><span>SEARCH PRODUCT</span>
    <svg width="7" height="7" viewBox="0 0 8 8"><circle cx="3.2" cy="3.2" r="2.4" fill="none" stroke="#9a9fa1"/><path d="M5 5l2.5 2.5" stroke="#9a9fa1"/></svg>
  </div>
</nav>

<section class="perks">
  <div class="perk"><span class="icon"><svg width="18" height="12" viewBox="0 0 18 12"><rect x="1" y="1" width="10" height="7" fill="#fff"/><path d="M11 3h4l2 3v2h-6z" fill="#fff"/><circle cx="4" cy="10" r="1.6" fill="#fff"/><circle cx="14" cy="10" r="1.6" fill="#fff"/></svg></span><div><h3>Free Shipping</h3><p>on orders $49 &amp; up</p></div></div>
  <div class="perk"><span class="icon"><svg width="16" height="16" viewBox="0 0 16 16"><path d="M13 8a5 5 0 1 1-2-4" fill="none" stroke="#fff" stroke-width="2"/><path d="M9 1l3 3-4 1z" fill="#fff"/></svg></span><div><h3>Easy Returns</h3><p>for up to 60 days</p></div></div>
  <div class="perk"><span class="icon"><svg width="14" height="16" viewBox="0 0 14 16"><rect x="1" y="7" width="12" height="8" rx="1" fill="#fff"/><path d="M4 7V5a3 3 0 0 1 6 0v2" fill="none" stroke="#fff" stroke-width="2"/></svg></span><div><h3>Secure Shopping</h3><p>shop with confidence</p></div></div>
</section>

<section class="hero">
  <div class="photo" role="img" aria-label="Photo of an infant in a white christening outfit and bonnet"></div>
  <div class="panel">
    <div class="copy">
      <span class="title">Spring Sale</span>
      <div class="deal">Discount upto <b>40%</b></div>
      <p class="blurb">Lorem ipsum dolor sit amet, consectetur adipiscing elit. Nulla nec vestibulum est, sed tempus dolor.</p>
      <a class="btn" href="#">Shop Now</a>
    </div>
    <div class="sprig" role="img" aria-label="Decorative spring flowers"></div>
  </div>
</section>
<div class="dots"><span></span><span></span><span></span><span></span><span></span></div>

<section class="promos">
  <div class="promo"><div class="pic" role="img" aria-label="Photo of a baby"></div><div class="txt"><h4><em>Special</em><br>Offers</h4><a class="btn" href="#">Shop now</a></div></div>
  <div class="promo"><div class="pic" role="img" aria-label="Photo of a baby in a sun hat"></div><div class="txt"><h4>Seasons <em>Sale</em></h4><p>Save upto 40%</p><a class="btn" href="#">Shop now</a></div></div>
  <div class="promo"><div class="pic" role="img" aria-label="Photo of a sleeping newborn"></div><div class="txt"><h4><em>Newborn</em><br>Gifts</h4><a class="btn" href="#">Shop now</a></div></div>
</section>

<section class="featured">
  <h2>FEATURED PRODUCTS</h2>
  <div class="grid">
    <article class="card"><div class="pic" role="img" aria-label="Product photo of white organza christening booties"></div><h5>Organza Trim Christening Bootie</h5><div class="price">$14.00</div><p>Lorem ipsum dolor sit amet,<br>consectetur adipiscing elit.</p><a class="btn" href="#">Add to cart</a></article>
    <article class="card"><div class="pic" role="img" aria-label="Product photo of a white christening bib"></div><h5>Organza Trim Christening Bootie</h5><div class="price">$14.00</div><p>Lorem ipsum dolor sit amet,<br>consectetur adipiscing elit.</p><a class="btn" href="#">Add to cart</a></article>
    <article class="card"><div class="pic" role="img" aria-label="Product photo of white baby shoes"></div><h5>Organza Trim Christening Bootie</h5><div class="price">$14.00</div><p>Lorem ipsum dolor sit amet,<br>consectetur adipiscing elit.</p><a class="btn" href="#">Add to cart</a></article>
    <article class="card"><div class="pic" role="img" aria-label="Product photo of a white christening outfit"></div><h5>Organza Trim Christening Bootie</h5><div class="price">$14.00</div><p>Lorem ipsum dolor sit amet,<br>consectetur adipiscing elit.</p><a class="btn" href="#">Add to cart</a></article>
  </div>
</section>

<footer class="footer">
  <div class="cols">
    <div>
      <h6>Connect With Us</h6>
      <div class="social"><span></span><span></span><span></span></div>
      <h6>Further Info</h6>
      <ul><li>Contact Us</li><li>Blog</li><li>Shipping &amp; Returns</li><li>Privacy Policy</li><li>Sitemap</li></ul>
    </div>
    <div>
      <h6>Categories</h6>
      <ul><li>New Baby</li><li>Christening &amp; Baptism</li><li>Birthday</li><li>Holiday</li><li>Wedding</li></ul>
    </div>
    <div>
      <h6>Brands</h6>
      <ul><li>Mavoret</li><li>View all brands</li></ul>
    </div>
    <div>
      <h6>Newsletter</h6>
      <input type="text" value="Your Name">
      <input type="text" value="Your Email">
      <a class="btn" href="#">Subscribe</a>
    </div>
  </div>
  <div class="legal">All prices are in USD. © 2015 Mavoret Childrenswear LLC</div>
</footer>

</body>
</html>
```